Banner Designs for Field Keep Ad Campaign

Harrowmere is a security consulting and services company that offers a service called FieldKeepUnit. FieldKeepUnit helps our customers secure large events by providing rapidly deployable security and communications technologies in a Field Keep vehicle, on a per event basis. We are looking for a designer to create a banner ad in three sizes for our campaign.
Target Market(s)
Our campaign is geared to the sports and entertainment industry, specifically large event venues and their security operation.
Industry/Entity Type
Security
Font styles to use
Other font styles liked:
- Raleway
Requirements
Must have
- Banner Objective
The visual and textual content of the banner should prompt the viewer to quickly identify the service offered and the information that is available to download.
Banner Design
Logo: FieldKeepUnit logo
Call to Action Button in Red: Get Details (On Right or or Upper Right)
Title in Larger Font: Take Control of you Events
Subtitle in smaller Font: Your Force Multiplier - Field Keep as a Service
Background: Photo of Field Keep interior or exterior or photo of female operator.
Font: Raleway
Banner Sizes
1 - 1200x670 pixels
2 - 1510x196 pixels
3 - 1200x628 pixels
Nice to have
- Follow the look and feel of the samples provided.

```html
<!DOCTYPE html>
<html lang="en">
<head>
<meta charset="utf-8">
<title>FieldKeepUnit – Take Control of You Events</title>
<link rel="stylesheet" href="https://fonts.googleapis.com/css2?family=Raleway:wght@300;400;500;700;800&family=Arimo:wght@700&display=swap">
<style>
  :root {
    --navy-deep: #070d1c;
    --navy: #0b1428;
    --brand-blue: #2f6db3;
    --white: #ffffff;
    --soft-white: #e8ecf3;
    --cta-red: #e3080f;
    --photo-dark: #23272e;
    --photo-mid: #4a4f58;
    --photo-light: #7c828c;
  }
  html, body {
    margin: 0;
    padding: 0;
    overflow: hidden;
    background: var(--navy-deep);
  }
  .banner {
    position: relative;
    width: 1200px;
    height: 670px;
    overflow: hidden;
    background: var(--navy-deep);
    font-family: "Raleway", sans-serif;
  }
  .banner__photo {
    position: absolute;
    left: 0;
    top: 0;
    width: 760px;
    height: 670px;
    background:
      radial-gradient(ellipse 260px 160px at 200px 300px, rgba(110,130,150,0.55), transparent 70%),
      radial-gradient(ellipse 200px 120px at 440px 300px, rgba(120,140,170,0.4), transparent 70%),
      linear-gradient(180deg, var(--photo-light) 0%, var(--photo-mid) 25%, var(--photo-dark) 60%, #17191e 100%);
  }
  .banner__fade {
    position: absolute;
    inset: 0;
    background: linear-gradient(90deg,
      rgba(7,13,28,0) 0%,
      rgba(7,13,28,0.15) 35%,
      rgba(7,13,28,0.75) 50%,
      var(--navy-deep) 60%,
      var(--navy) 100%);
  }
  .banner__content {
    position: absolute;
    left: 700px;
    top: 0;
    width: 450px;
    height: 670px;
    text-align: center;
    color: var(--white);
  }
  .brand {
    position: absolute;
    left: 30px;
    top: 112px;
    width: 400px;
    text-align: left;
  }
  .brand__name {
    display: flex;
    align-items: center;
    gap: 12px;
    font-size: 42px;
    font-weight: 500;
    letter-spacing: -0.5px;
    color: var(--white);
    line-height: 1;
  }
  .brand__dot {
    width: 16px;
    height: 16px;
    border-radius: 50%;
    background: var(--brand-blue);
  }
  .brand__by {
    margin: 10px 0 0 310px;
    font-size: 16px;
    font-weight: 500;
    color: var(--soft-white);
  }
  .headline {
    position: absolute;
    left: 0;
    top: 252px;
    width: 450px;
    margin: 0;
    font-size: 53px;
    line-height: 1.06;
    text-transform: uppercase;
  }
  .headline__accent {
    display: block;
    font-weight: 800;
    color: var(--brand-blue);
  }
  .headline__rest {
    display: block;
    font-weight: 300;
    color: var(--white);
  }
  .subtitle {
    position: absolute;
    left: 0;
    top: 420px;
    width: 450px;
    margin: 0;
    font-size: 19px;
    font-weight: 500;
    line-height: 1.3;
    letter-spacing: 0.3px;
    color: var(--soft-white);
  }
  .cta {
    position: absolute;
    left: 102px;
    top: 533px;
    width: 242px;
    height: 58px;
    display: flex;
    align-items: center;
    justify-content: center;
    background: var(--cta-red);
    color: var(--white);
    font-family: "Arimo", sans-serif;
    font-weight: 700;
    font-size: 32px;
    text-decoration: none;
    box-shadow: 0 4px 10px rgba(0,0,0,0.45);
  }
</style>
</head>
<body>
  <main class="banner">
    <div class="banner__photo" role="img" aria-label="Interior of a Field Keep vehicle: operator workstation with monitors showing maps and camera feeds, radios, cabinets and mesh office chairs"></div>
    <div class="banner__fade"></div>

    <section class="banner__content">
      <div class="brand">
        <div class="brand__name"><span class="brand__dot"></span>FieldKeepUnit</div>
        <div class="brand__by">By Harrowmere</div>
      </div>

      <h1 class="headline">
        <span class="headline__accent">Take Control</span>
        <span class="headline__rest">Of You Events</span>
      </h1>

      <p class="subtitle">Your Force Multiplier<br>Field Keep as a Service</p>

      <a class="cta" href="#details">Get Details</a>
    </section>
  </main>
</body>
</html>
```